Healthy Lifestyle Vitamin Supplement Company needs a web site designed.

We are starting a new website for selling quality natural vitamins and supplements online plus providing news and information on healthy living. We DO NOT need any programming done for this site. Just the design in a layered photoshop file. This site needs to communicate that we are the authoritative source for healthy living and a trusted place to buy supplements and information on living a healthy lifestyle.

Triggers On page will be

Trigger set 1
Home - Shop By Brand - Top Sellers - Clearance - Help Center - My Favorites

Trigger set 2
Vitamins and Herbs - Natural Living - Aromatherapy - Coffee and Tea - Health and Beauty - Healthy Foods - Pet Health - Sports and Diet

Triggers Other
Login - Shopping Cart - Checkout - Track Order

Need a search bar in the design

Left side should be categories look at Brelvox.com for example of categories.

Name and domain name is Sunward Meadow Crest

Will also need a logo to go along with that.

Industry/Entity Type

It Company

```html
<!DOCTYPE html>
<html lang="en">
<head>
<meta charset="utf-8">
<title>Sunward Meadow Crest – Natural Vitamins and Supplements</title>
<link href="https://fonts.googleapis.com/css2?family=Open+Sans:wght@400;600;700;800&display=swap" rel="stylesheet">
<style>
:root{
  --blue:#1c9fe0;
  --blue-dark:#137fc0;
  --green:#8cc63f;
  --green-dark:#6aa22b;
  --ink:#333;
  --muted:#777;
  --line:#e2e2e2;
  --top:#2a2a2a;
  --footer:#2d2d2d;
  --footer-deep:#232323;
  --paper:#fff;
  --soft:#f4f4f4;
  --red:#e43c2f;
}
*{box-sizing:border-box;margin:0;padding:0}
html,body{width:1200px;height:2959px;overflow:hidden}
body{font-family:"Open Sans",Arial,sans-serif;color:var(--ink);background:var(--paper);position:relative;font-size:13px}
a{color:inherit;text-decoration:none}
.wrap{position:absolute;left:105px;width:990px}

/* top bar */
.topbar{position:absolute;top:0;left:0;width:1200px;height:32px;background:var(--top);color:#fff;font-size:11px;font-weight:700}
.topbar .links{position:absolute;right:105px;top:9px;letter-spacing:.3px}
.topbar .links span{margin:0 6px;color:#888}

/* header */
.brand{top:45px;width:390px;height:60px;display:flex;align-items:center;gap:10px}
.brand .dot{width:36px;height:36px;border-radius:50%;background:var(--green);flex:none}
.brand .name{font-size:22px;font-weight:800;color:var(--green-dark);letter-spacing:.3px;white-space:nowrap}
.search{position:absolute;left:510px;top:48px;width:270px;height:32px;border:1px solid #ccc;display:flex}
.search .field{flex:1;padding:7px 10px;color:#999;font-size:12px}
.search .btn{width:34px;background:var(--soft);border-left:1px solid #ccc;display:flex;align-items:center;justify-content:center}
.cart{position:absolute;left:805px;top:50px;width:290px;height:28px;display:flex;align-items:center;gap:8px;font-size:13px}
.cart .sep{border-left:1px solid #bbb;height:16px}
.cart .checkout{font-weight:700;text-decoration:underline}

.catnav{top:112px;height:22px;display:flex;justify-content:space-between;font-size:12px;font-weight:600;color:#444}
.catnav i{font-style:normal;color:#999;font-size:10px;margin-left:3px}

.mainnav{top:143px;height:32px;background:var(--blue);display:flex}
.mainnav a{color:#fff;font-size:12px;font-weight:700;text-transform:uppercase;padding:0 22px;line-height:32px;border-right:1px solid rgba(255,255,255,.25)}
.mainnav a.active{background:var(--green)}

/* hero */
.hero{top:190px;height:330px;background:linear-gradient(100deg,#b5cc6a 0%,#e3eab8 40%,#cfe0a0 70%,#8fb55a 100%);overflow:hidden}
.hero .photo{position:absolute;left:0;top:0;width:520px;height:330px;background:radial-gradient(circle at 50% 45%,#ffffff 0%,#f4f7e6 40%,rgba(200,220,140,0) 75%)}
.hero .free{position:absolute;left:8px;top:195px;width:130px;height:90px;background:var(--red);transform:rotate(-12deg);color:#fff;font-weight:800;font-size:18px;line-height:21px;padding:12px 14px}
.hero .free small{display:block;font-size:13px;font-weight:700}
.hero h1{position:absolute;left:540px;top:75px;width:420px;font-size:40px;line-height:48px;font-weight:700;color:#2d5d1b}
.hero .cta{position:absolute;left:640px;top:230px;background:var(--blue);color:#fff;font-weight:700;font-size:16px;padding:8px 22px}
.hero .dots{position:absolute;right:20px;bottom:14px;display:flex;gap:6px}
.hero .dots b{width:9px;height:9px;border-radius:50%;background:rgba(255,255,255,.7)}
.hero .dots b.on{background:#fff}

/* feature tiles */
.tiles{top:538px;height:180px;display:flex;gap:12px}
.tile{flex:1;position:relative}
.tile .img{height:140px}
.tile .label{height:40px;background:var(--blue);color:#fff;font-weight:700;font-size:15px;text-align:center;line-height:40px}
.t1 .img{background:linear-gradient(135deg,#5a3a24,#a87748 60%,#e9d7b6)}
.t2 .img{background:linear-gradient(135deg,#cfe6ef,#88b3c4 60%,#e8f2f5)}
.t3 .img{background:linear-gradient(135deg,#d6d6d6,#8a8a8a 55%,#e6e6e6)}
.t4 .img{background:linear-gradient(135deg,#e6c44a,#7cae3c 50%,#d9573a)}

/* sidebar */
.sidebar{position:absolute;left:118px;top:762px;width:215px;height:1005px;border:1px solid var(--line);background:#fafafa}
.sidebar h3{font-size:12px;font-weight:800;padding:12px 14px 10px;border-bottom:2px solid var(--green);display:flex;align-items:center;gap:6px}
.sidebar ul{list-style:none;padding:4px 14px}
.sidebar li{font-size:11.5px;color:#555;line-height:23.4px;border-bottom:1px dotted #ddd}

/* products */
.grid{position:absolute;left:350px;top:762px;width:745px;display:grid;grid-template-columns:repeat(3,235px);column-gap:20px;row-gap:22px}
.card{position:relative;height:325px;border:1px solid var(--line);overflow:hidden;background:#fff}
.card .head{display:flex;align-items:center;gap:7px;padding:10px 12px;font-weight:700;font-size:14px}
.card .ribbon{position:absolute;right:-28px;top:14px;width:100px;transform:rotate(45deg);background:var(--green);color:#fff;font-size:10px;font-weight:700;text-align:center;line-height:18px}
.card .pic{margin:4px auto 0;width:105px;height:128px;border-radius:10px 10px 6px 6px}
.pic.brown{background:linear-gradient(180deg,#5b2b15,#b2582a 55%,#6a3018)}
.pic.amber{background:linear-gradient(180deg,#3a2410,#c4661e 55%,#7b3f12)}
.pic.white{background:linear-gradient(180deg,#eee,#fff 40%,#6f8a3b 45%,#dfe6cc)}
.card .title{display:flex;align-items:center;justify-content:center;text-align:center;color:var(--blue);font-size:12px;font-weight:600;line-height:16px;margin-top:10px;padding:0 14px;height:32px}
.card .retail{text-align:center;font-size:11px;line-height:15px;color:#999;margin-top:5px;text-decoration:line-through}
.card .price{text-align:center;font-size:18px;line-height:24px;font-weight:700;color:var(--green-dark);margin-top:1px}
.card .btns{position:absolute;bottom:12px;left:0;right:0;display:flex;justify-content:center;gap:10px}
.card .btns span{font-size:10px;font-weight:700;padding:6px 12px}
.btn-shop{background:#e6e6e6;color:#555}
.btn-read{background:var(--blue);color:#fff}

.pager{position:absolute;left:830px;top:1790px;display:flex;gap:6px}
.pager span{width:30px;height:30px;border:1px solid #ccc;font-size:13px;text-align:center;line-height:28px}
.pager span.on{background:#888;color:#fff;border-color:#888}

/* news band */
.news{position:absolute;left:0;top:1890px;width:1200px;height:110px;background:var(--green)}
.news .tag{position:absolute;left:118px;top:28px;width:200px;height:54px;background:#fff;border-left:6px solid var(--blue);color:var(--blue);font-weight:800;font-size:19px;line-height:54px;padding-left:18px}
.news p{position:absolute;left:350px;top:22px;width:745px;color:#fff;font-size:12px;font-weight:600;line-height:19px;text-align:center}

/* info row */
.info{top:2023px;height:120px;display:flex;justify-content:space-between;padding:0 13px}
.info .col{width:300px}
.info h4{color:var(--blue);font-size:15px;font-weight:600;margin-bottom:6px}
.info p{font-size:11.5px;color:#666;line-height:17px}
.signup{margin-top:18px;display:flex}
.signup .field{width:220px;height:30px;border:1px solid #ccc;font-size:11px;color:#aaa;padding:7px 10px}
.signup .go{background:var(--blue);color:#fff;font-size:10px;font-weight:700;padding:0 14px;line-height:30px}
.social{display:flex;gap:20px;margin-top:18px}
.social b{width:34px;height:34px;border-radius:50%;background:var(--blue)}

/* footer */
.footer{position:absolute;left:0;top:2165px;width:1200px;height:794px;background:var(--footer);color:#ccc}
.fcols{position:absolute;left:118px;top:28px;width:980px;display:flex}
.fcol{width:210px}
.fcol h5{font-size:14px;font-weight:600;color:#fff;margin-bottom:10px}
.fcol li{list-style:none;font-size:11.5px;line-height:17px}
.flogo{position:absolute;left:870px;top:75px;display:flex;align-items:center;gap:10px}
.flogo .dot{width:30px;height:30px;border-radius:50%;background:#fff}
.flogo span{color:#fff;font-weight:800;font-size:17px}
.badges{position:absolute;left:105px;top:262px;width:990px;height:58px;display:flex;align-items:center;justify-content:space-between}
.badge{height:40px;border-radius:4px;background:#4a4a4a}
.pay{display:flex;gap:10px;align-items:center}
.pay .word{color:#fff;font-weight:800;font-size:30px;margin-right:30px}
.pay .cardshape{width:52px;height:34px;border-radius:4px;background:#d8d8d8}
.legal{position:absolute;left:118px;width:965px;font-size:11px;line-height:16px;color:#ddd;text-align:center}
.legal b{color:#fff}
.strip{position:absolute;left:0;bottom:0;width:1200px;height:36px;background:var(--footer-deep);font-size:11px;color:#bbb;padding:11px 118px}
</style>
</head>
<body>

<div class="topbar"><div class="links">PHONE: 0800 555 0142<span>|</span>LOGIN<span>|</span>REGISTER<span>|</span>TRACK ORDER</div></div>

<div class="wrap brand"><div class="dot"></div><div class="name">SUNWARD MEADOW CREST</div></div>

<div class="search"><div class="field">Search</div><div class="btn">
<svg width="14" height="14" viewBox="0 0 14 14"><circle cx="6" cy="6" r="4.5" fill="none" stroke="#666" stroke-width="1.6"/><line x1="9.3" y1="9.3" x2="13" y2="13" stroke="#666" stroke-width="1.8"/></svg></div></div>
<div class="cart">
<svg width="18" height="16" viewBox="0 0 18 16"><path d="M1 2h3l2 8h9l2-6H5" fill="none" stroke="#555" stroke-width="1.5"/><circle cx="7" cy="13.5" r="1.5" fill="#555"/><circle cx="14" cy="13.5" r="1.5" fill="#555"/></svg>
<span>My Cart (0)</span><span class="sep"></span><span class="checkout">Checkout</span></div>

<nav class="wrap catnav">
<a>Vitamins and Herbs<i>▾</i></a><a>Natural Living<i>▾</i></a><a>Aromatherapy<i>▾</i></a><a>Coffee and Tea<i>▾</i></a><a>Health and Beauty<i>▾</i></a><a>Healthy Foods<i>▾</i></a><a>Pet Health<i>▾</i></a><a>Sports and Diet<i>▾</i></a>
</nav>

<nav class="wrap mainnav">
<a class="active">Home</a><a>Shop by Brand</a><a>Top Sellers</a><a>Clearance</a><a>Help Center</a><a>My Favorites</a>
</nav>

<section class="wrap hero">
<div class="photo" role="img" aria-label="Two tubs of greens supplement powder on a leafy background"></div>
<div class="free">FREE<small>Shipping on all orders</small></div>
<h1>Selling Quality Natural Vitamins and Supplements</h1>
<a class="cta">SHOP NOW</a>
<div class="dots"><b class="on"></b><b></b><b></b><b></b><b></b></div>
</section>

<section class="wrap tiles">
<div class="tile t1"><div class="img" role="img" aria-label="Coffee beans and a cup of tea"></div><div class="label">Coffee &amp; Teas</div></div>
<div class="tile t2"><div class="img" role="img" aria-label="Essential oil bottles with flowers"></div><div class="label">Essential Oils</div></div>
<div class="tile t3"><div class="img" role="img" aria-label="Protein powder scoop"></div><div class="label">Protein</div></div>
<div class="tile t4"><div class="img" role="img" aria-label="Fresh fruit and vegetables"></div><div class="label">New Healthy Foods</div></div>
</section>

<aside class="sidebar">
<h3><svg width="12" height="12" viewBox="0 0 12 12"><path d="M2 10C2 4 6 1 11 1 11 7 7 10 2 10z" fill="var(--green)"/></svg>CATEGORIES</h3>
<ul>
<li>A-B-C Vitamins</li><li>Acidophilus/Probiotics</li><li>Amino Acid Supplements</li><li>Antioxidants</li><li>B Vitamins</li><li>B-12 Vitamins</li><li>B-Complex Vitamins</li><li>Babies &amp; Kids</li><li>C Vitamins</li><li>Calcium Supplements</li><li>Co Q-10</li><li>D Vitamins</li><li>Diet &amp; Lifestyle</li><li>Digestive Health</li><li>E Vitamins</li><li>Eye Health</li><li>Fish Oils</li><li>Garcinia Cambogia</li><li>Health &amp; Beauty</li><li>Herbal Supplements</li><li>Joint Support</li><li>L-Carnitine</li><li>Magnesium</li><li>Medicine Cabinet</li><li>Men's Vitamins</li><li>Mental Focus</li><li>Multivitamins</li><li>Omega 3 Products</li><li>Organic, Vegetarian, Non-GMO</li><li>Sexual Health</li><li>Turmeric</li><li>Women's Vitamins</li>
</ul>
</aside>

<main class="grid">
<div class="card"><div class="head"><svg width="14" height="14"><circle cx="7" cy="7" r="6" fill="var(--green)"/></svg>Heart Health</div><div class="ribbon">NEW</div><div class="pic brown" role="img" aria-label="Niacin supplement bottle"></div><div class="title">Flush Free Niacin Inositol Hexanicotinate 1000 mg</div><div class="retail">Retail $35.40</div><div class="price">$22.50</div><div class="btns"><span class="btn-shop">SHOP NOW</span><span class="btn-read">READ MORE</span></div></div>
<div class="card"><div class="head"><svg width="14" height="14"><circle cx="7" cy="7" r="6" fill="var(--green)"/></svg>Omega-3</div><div class="pic amber" role="img" aria-label="Omega-3 fish oil bottle"></div><div class="title">Maximum Strength Triple Omega 3-6-9 Fish</div><div class="retail">Retail $35.40</div><div class="price">$22.50</div><div class="btns"><span class="btn-shop">SHOP NOW</span><span class="btn-read">READ MORE</span></div></div>
<div class="card"><div class="head"><svg width="14" height="14"><circle cx="7" cy="7" r="6" fill="var(--green)"/></svg>Diet &amp; Lifestyle</div><div class="ribbon">NEW</div><div class="pic white" role="img" aria-label="Raspberry ketones supplement bottle"></div><div class="title">Raspberry Ketones 500 mg</div><div class="retail">Retail $35.40</div><div class="price">$22.50</div><div class="btns"><span class="btn-shop">SHOP NOW</span><span class="btn-read">READ MORE</span></div></div>

<div class="card"><div class="head"><svg width="14" height="14"><circle cx="7" cy="7" r="6" fill="var(--green)"/></svg>Eye Health</div><div class="ribbon">NEW</div><div class="pic white" role="img" aria-label="Lutein supplement bottle"></div><div class="title">Lutein 20 mg with Zeaxanthin</div><div class="retail">Retail $35.40</div><div class="price">$22.50</div><div class="btns"><span class="btn-shop">SHOP NOW</span><span class="btn-read">READ MORE</span></div></div>
<div class="card"><div class="head"><svg width="14" height="14"><circle cx="7" cy="7" r="6" fill="var(--green)"/></svg>Health &amp; Beauty</div><div class="pic brown" role="img" aria-label="Facial oil bottle"></div><div class="title">Flush Free Facial Oil 1000 mg</div><div class="retail">Retail $35.40</div><div class="price">$22.50</div><div class="btns"><span class="btn-shop">SHOP NOW</span><span class="btn-read">READ MORE</span></div></div>
<div class="card"><div class="head"><svg width="14" height="14"><circle cx="7" cy="7" r="6" fill="var(--green)"/></svg>Digestive Health</div><div class="pic white" role="img" aria-label="Probiotic supplement bottle"></div><div class="title">Probiotic Acidophilus</div><div class="retail">Retail $35.40</div><div class="price">$22.50</div><div class="btns"><span class="btn-shop">SHOP NOW</span><span class="btn-read">READ MORE</span></div></div>

<div class="card"><div class="head"><svg width="14" height="14"><circle cx="7" cy="7" r="6" fill="var(--green)"/></svg>Heart Health</div><div class="pic brown" role="img" aria-label="Niacin supplement bottle"></div><div class="title">Flush Free Niacin Inositol Hexanicotinate 1000 mg</div><div class="retail">Retail $35.40</div><div class="price">$22.50</div><div class="btns"><span class="btn-shop">SHOP NOW</span><span class="btn-read">READ MORE</span></div></div>
<div class="card"><div class="head"><svg width="14" height="14"><circle cx="7" cy="7" r="6" fill="var(--green)"/></svg>Omega-3</div><div class="ribbon">NEW</div><div class="pic amber" role="img" aria-label="Omega-3 fish oil bottle"></div><div class="title">Maximum Strength Triple Omega 3-6-9 Fish</div><div class="retail">Retail $35.40</div><div class="price">$22.50</div><div class="btns"><span class="btn-shop">SHOP NOW</span><span class="btn-read">READ MORE</span></div></div>
<div class="card"><div class="head"><svg width="14" height="14"><circle cx="7" cy="7" r="6" fill="var(--green)"/></svg>Diet &amp; Lifestyle</div><div class="pic white" role="img" aria-label="Raspberry ketones supplement bottle"></div><div class="title">Raspberry Ketones 500 mg</div><div class="retail">Retail $35.40</div><div class="price">$22.50</div><div class="btns"><span class="btn-shop">SHOP NOW</span><span class="btn-read">READ MORE</span></div></div>
</main>

<div class="pager"><span class="on">1</span><span>2</span><span>3</span><span>4</span><span>5</span><span>6</span><span>&gt;&gt;</span></div>

<section class="news">
<div class="tag">IN THE NEWS</div>
<p>Lorem ipsum dolor sit amet, consectetur adipiscing elit, sed do eiusmod tempor incididunt ut labore et dolore magna aliqua. Ut enim ad minim veniam, quis nostrud exercitation ullamco laboris nisi ut aliquip ex ea commodo consequat. Duis aute irure dolor in reprehenderit in voluptate velit esse cillum.</p>
</section>

<section class="wrap info">
<div class="col"><h4>Email Sign-Up</h4><p>Be the first to receive special discounts</p><div class="signup"><div class="field">Enter your email ID</div><div class="go">SUBSCRIBE</div></div></div>
<div class="col"><h4>Contact Us</h4><p>416 st, Lorem ipsum madddar ca 123456<br>Phone:+1 555 014 2200<br>Email: info@sunwardmeadowcrest.com</p></div>
<div class="col"><h4>Stay Connected</h4><p>Find out what people are saying</p><div class="social"><b aria-label="Social network one"></b><b aria-label="Social network two"></b><b aria-label="Social network three"></b><b aria-label="Social network four"></b></div></div>
</section>

<footer class="footer">
<div class="fcols">
<div class="fcol"><h5>Company Info</h5><ul><li>About Us</li><li>Affiliate Program</li><li>Contact Us</li><li>Quality Guarantee</li><li>CSPR</li><li>International Distribution</li></ul></div>
<div class="fcol"><h5>Customer Service</h5><ul><li>Price Match Guarantee</li><li>Coupon Policy</li><li>Help Center</li></ul></div>
<div class="fcol"><h5>My Account</h5><ul><li>Log In</li><li>Auto Delivery</li><li>Create Account</li><li>My Favorites</li><li>Order History</li><li>Track Order</li><li>Sweepstakes</li></ul></div>
<div class="fcol"><h5>Shipping &amp; Returns</h5><ul><li>International Shipping</li><li>Lost or Damaged</li><li>Return Policy</li><li>Shipping Information</li></ul></div>
</div>
<div class="flogo"><div class="dot"></div><span>SUNWARD MEADOW CREST</span></div>

<div class="badges">
<div class="badge" style="width:130px" aria-label="Privacy certification badge"></div>
<div class="badge" style="width:140px" aria-label="Security certification badge"></div>
<div class="pay"><span class="word">Secure Pay</span><span class="cardshape"></span><span class="cardshape"></span><span class="cardshape"></span><span class="cardshape"></span></div>
</div>

<p class="legal" style="top:345px"><b>* Sunward Meadow Crest provides these articles for information only. They are not approved or recommended by us, do not provide medical advice, diagnosis, or treatment, and are not meant to replace professional medical advice or apply to any products.</b></p>
<p class="legal" style="top:410px">**These statements have not been evaluated by the Food and Drug Administration. These products are not intended to diagnose, treat, cure or prevent any disease.</p>
<p class="legal" style="top:455px;text-align:left">The information provided on this site is intended for your general knowledge only and is not a substitute for professional medical advice or treatment for specific medical conditions. Always seek the advice of your physician or other qualified health care provider with any questions you may have regarding a medical condition. The information on this website is not intended to diagnose, treat, cure or prevent any disease. Never disregard medical advice or delay in seeking it because of something you have read on the Sunward Meadow Crest site. Product sold on this site are for personal use and not for resale. All orders placed through this website are subject to Sunward Meadow Crest acceptance, in its sole discretion. This means that Sunward Meadow Crest may refuse to accept, or may cancel, any order, whether or not it has been confirmed, without liability to you or any third party. Sunward Meadow Crest reserves the right to discontinue any program or offer.</p>
<p class="legal" style="top:600px">If you would like to unsubscribe from future Sunward Meadow Crest emails, please click here to unsubscribe.</p>
<p class="legal" style="top:640px;text-align:left">* Same item, same size Sunward Meadow Crest® brand products, discount already reflected in the applicable product price. Certain products, including clearance section items, may be excluded. All products subject to availability. To expedite orders, we may substitute smaller bottles if ordered quantity is out of stock. Terms and conditions subject to change. Free Shipping offers apply within the contiguous 48 U.S. states; will automatically apply to your cart at checkout; not valid on orders.</p>
<div class="strip">Copyright 2014 Sunward Meadow Crest, Inc.|Customer Service 1-555-014-2201 | Privacy Policy | Terms of Use</div>
</footer>

</body>
</html>
```